Green Energy Conservation Business Cards

We believe in Conserve before you produce energy. I am looking for a unique, bold business card. that Demonstrates Expertise in our field. I would be interested to try and incorporate a night picture of the US or world showing the yellow lights on one side. I would be open to a design that caters to half the business card size height and same length. Our primary expertise is Energy projects for self storage. Use either black or white background .Attached are the logos and symbols.

May I see some design utilizing a smaller business card. the same length as a normal business card but cut in half on the height. best regards Garvel

```html
<!DOCTYPE html>
<html lang="en">
<head>
<meta charset="utf-8">
<title>Verdant Energy Group – Business Card</title>
<link href="https://fonts.googleapis.com/css2?family=Arimo:wght@400;700&display=swap" rel="stylesheet">
<style>
  :root {
    --backdrop: #ececec;
    --card: #ffffff;
    --navy: #1a4fa0;
    --green: #6cb33f;
    --green-light: #b5d334;
    --shadow: rgba(0,0,0,0.12);
  }
  * { margin: 0; padding: 0; box-sizing: border-box; }
  html, body {
    width: 1200px; height: 972px; overflow: hidden;
    background: var(--backdrop);
    font-family: "Arimo", Arial, sans-serif;
  }
  .stage { position: relative; width: 1200px; height: 972px; }
  .card {
    position: absolute;
    width: 560px; height: 320px;
    background: var(--card);
    box-shadow: 0 6px 18px var(--shadow);
  }
  .card--front { left: 70px; top: 120px; }
  .card--back { left: 570px; top: 520px; }

  .brand {
    position: absolute; left: 80px; top: 118px;
    display: flex; align-items: center; gap: 18px;
  }
  .brand-dot {
    width: 64px; height: 64px; border-radius: 50%; flex: none;
    background: linear-gradient(160deg, var(--green), var(--green-light));
  }
  .brand-name {
    font-weight: 700; font-size: 40px; line-height: 1.05;
    color: var(--navy); letter-spacing: 0.5px;
  }

  .emblem {
    position: absolute; left: 48px; top: 62px;
    width: 196px; height: 196px; border-radius: 50%;
    background: linear-gradient(160deg, var(--green), var(--green-light));
  }
  .contact { position: absolute; left: 290px; top: 56px; }
  .person-name { font-weight: 700; font-size: 19px; color: var(--navy); }
  .person-title { font-size: 18px; color: var(--navy); margin-top: 2px; }
  .details { list-style: none; margin-top: 26px; }
  .details li {
    display: flex; align-items: flex-start; gap: 9px;
    font-size: 16px; line-height: 1.2; color: var(--green);
    margin-bottom: 12px;
  }
  .details svg { flex: none; width: 14px; height: 14px; margin-top: 2px; }
</style>
</head>
<body>
<main class="stage">
  <section class="card card--front">
    <div class="brand">
      <span class="brand-dot"></span>
      <span class="brand-name">Verdant<br>Energy Group</span>
    </div>
  </section>

  <section class="card card--back">
    <div class="emblem"></div>
    <div class="contact">
      <p class="person-name">Marcus Hollen</p>
      <p class="person-title">President</p>
      <ul class="details">
        <li>
          <svg viewBox="0 0 14 14" aria-hidden="true"><circle cx="7" cy="7" r="7" fill="#6cb33f"/><path d="M7 3a2.5 2.5 0 0 0-2.5 2.5C4.5 7.5 7 11 7 11s2.5-3.5 2.5-5.5A2.5 2.5 0 0 0 7 3z" fill="#fff"/><circle cx="7" cy="5.5" r="1" fill="#6cb33f"/></svg>
          <span>418 W Maple St<br>Riverbend CA 95012</span>
        </li>
        <li>
          <svg viewBox="0 0 14 14" aria-hidden="true"><circle cx="7" cy="7" r="7" fill="#6cb33f"/><path d="M4.5 3.5l1.6-.3.8 2-1 .8a5 5 0 0 0 2.1 2.1l.8-1 2 .8-.3 1.6c-3.2.3-6.3-2.8-6-6z" fill="#fff"/></svg>
          <span>(555)214-0372</span>
        </li>
        <li>
          <svg viewBox="0 0 14 14" aria-hidden="true"><circle cx="7" cy="7" r="7" fill="#6cb33f"/><rect x="3.5" y="4.5" width="7" height="5" fill="#fff"/><path d="M3.5 4.5L7 7.3l3.5-2.8" fill="none" stroke="#6cb33f" stroke-width="0.8"/></svg>
          <span>marcus@verdantenergy.com</span>
        </li>
      </ul>
    </div>
  </section>
</main>
</body>
</html>
```